We need a nice stationary and business card design for our new mobile ultrasound company.
Kestral Sonics, LLC
We need a nice stationary and business card design for our new mobile ultrasound company.  - Medical
Creative Brief
Bright & Fun-filled
Tomaso Fairbank
Vice President
5817 E. Halvering Ct
Tomaso.Fairbank@kestralsonics.example
KestralSonics.example
Please do not add our address to your design.

```html
<!DOCTYPE html>
<html lang="en">
<head>
<meta charset="utf-8">
<title>Kestral Sonics Stationery</title>
<link rel="stylesheet" href="https://fonts.googleapis.com/css2?family=Open+Sans:wght@400;600&display=swap">
<style>
  :root {
    --page: #ffffff;
    --paper: #ffffff;
    --edge: #d9dde2;
    --brand: #1d6db3;
    --brand-light: #4aa3df;
    --ink: #555b61;
    --fold: #b9bfc6;
  }
  html, body { margin: 0; padding: 0; overflow: hidden; }
  body {
    width: 1200px; height: 681px; position: relative;
    background: var(--page);
    font-family: "Open Sans", Arial, sans-serif;
    color: var(--ink);
  }
  .piece {
    position: absolute; background: var(--paper);
    border: 1px solid var(--edge); box-sizing: border-box; overflow: hidden;
  }
  .brand {
    display: flex; align-items: center; gap: 6px;
    color: var(--brand); font-weight: 600; white-space: nowrap;
  }
  .brand-dot { border-radius: 50%; background: var(--brand); flex: none; }
  .contact { font-size: 7px; line-height: 9.5px; white-space: nowrap; }
  .stripe-thin { position: absolute; left: 0; right: 0; height: 3px; background: var(--brand-light); }
  .stripe-thick { position: absolute; left: 0; right: 0; height: 9px; background: var(--brand); }
  .centre-dot {
    position: absolute; border-radius: 50%; background: var(--brand);
    left: 50%; transform: translateX(-50%);
  }

  /* Envelope front */
  .envelope-front { left: 60px; top: 96px; width: 497px; height: 216px; }
  .envelope-front .brand { position: absolute; left: 16px; top: 16px; font-size: 20px; }
  .envelope-front .brand-dot { width: 20px; height: 20px; }
  .envelope-front .contact { position: absolute; left: 18px; top: 58px; }
  .envelope-front .stripe-thin { top: 178px; }
  .envelope-front .stripe-thick { top: 185px; }

  /* Envelope back */
  .envelope-back { left: 60px; top: 372px; width: 497px; height: 211px; }
  .envelope-back .flap { position: absolute; left: 0; top: 0; width: 100%; height: 90px; }
  .envelope-back .centre-dot { top: 30px; width: 34px; height: 34px; }

  /* Letterhead */
  .letterhead { left: 619px; top: 41px; width: 312px; height: 583px; }
  .letterhead .brand { position: absolute; left: 18px; top: 24px; font-size: 18px; }
  .letterhead .brand-dot { width: 18px; height: 18px; }
  .letterhead .contact { position: absolute; left: 20px; top: 62px; }
  .letterhead .stripe-thin { top: 541px; }
  .letterhead .stripe-thick { top: 548px; }

  /* Business card front */
  .card-front { left: 967px; top: 252px; width: 156px; height: 84px; }
  .card-front .brand { position: absolute; left: 8px; top: 31px; font-size: 7.5px; gap: 3px; }
  .card-front .brand-dot { width: 8px; height: 8px; }
  .card-front .holder { position: absolute; left: 78px; top: 10px; font-size: 5px; line-height: 6.5px; white-space: nowrap; }
  .card-front .contact { position: absolute; left: 78px; top: 34px; font-size: 3.4px; line-height: 5px; }

  /* Business card back */
  .card-back { left: 967px; top: 365px; width: 156px; height: 84px; }
  .card-back .centre-dot { top: 26px; width: 30px; height: 30px; }
</style>
</head>
<body>

<section class="piece envelope-front">
  <div class="brand"><span class="brand-dot"></span>Kestral Sonics</div>
  <div class="contact">
    Phone: (555) 014-2290<br>
    Fax: (555) 014-2291<br>
    Tomaso.Fairbank@kestralsonics.example<br>
    KestralSonics.example
  </div>
  <div class="stripe-thin"></div>
  <div class="stripe-thick"></div>
</section>

<section class="piece envelope-back">
  <svg class="flap" viewBox="0 0 497 90" preserveAspectRatio="none">
    <path d="M0 0 L20 70 Q24 82 40 82 L457 82 Q473 82 477 70 L497 0" fill="none" stroke="var(--fold)" stroke-width="1"/>
  </svg>
  <div class="centre-dot"></div>
</section>

<section class="piece letterhead">
  <div class="brand"><span class="brand-dot"></span>Kestral Sonics</div>
  <div class="contact">
    Phone: (555) 014-2290<br>
    Fax: (555) 014-2291<br>
    Tomaso.Fairbank@kestralsonics.example<br>
    KestralSonics.example
  </div>
  <div class="stripe-thin"></div>
  <div class="stripe-thick"></div>
</section>

<section class="piece card-front">
  <div class="holder">Tomaso Fairbank<br>Vice President</div>
  <div class="brand"><span class="brand-dot"></span>Kestral Sonics</div>
  <div class="contact">
    Phone: (555) 014-2290<br>
    Fax: (555) 014-2291<br>
    Tomaso.Fairbank@kestralsonics.example<br>
    KestralSonics.example
  </div>
</section>

<section class="piece card-back">
  <div class="centre-dot"></div>
</section>

</body>
</html>
```